Tampa, Florida based Real Estate company Business Cards

Need ideas for real estate business cards
Updates

Need extra days to review

Industry/Entity Type

Real Estate

Contact Information for Business Card

Space for image, space for logo, contact information space

Font styles to use
Sans Serif

Colors

Designer to choose colors to be used in the design.

Requirements
Must have
• Options to have duplicate content on the back of card for a team of agents.

```html
<!DOCTYPE html>
<html lang="en">
<head>
<meta charset="utf-8">
<title>Harborline Realty – Business Cards</title>
<link href="https://fonts.googleapis.com/css2?family=Raleway:wght@300;400;800&display=swap" rel="stylesheet">
<style>
  :root {
    --backdrop: #d6d6d6;
    --paper: #ffffff;
    --navy: #1e1c48;
    --silver: #c9c9cc;
    --divider: #d4d4d8;
  }
  * { box-sizing: border-box; margin: 0; padding: 0; }
  html, body { width: 1200px; height: 846px; overflow: hidden; }
  body {
    background: var(--backdrop);
    font-family: 'Raleway', sans-serif;
    position: relative;
  }
  .card {
    position: absolute;
    width: 540px;
    height: 309px;
    box-shadow: 0 10px 24px rgba(0,0,0,0.18);
  }
  .card--front { left: 50px; top: 150px; background: var(--paper); }
  .card--back { left: 610px; top: 387px; background: var(--navy); overflow: hidden; }

  .brand {
    position: absolute;
    left: 40px; top: 120px;
    width: 200px;
    text-align: center;
    color: var(--navy);
    font-weight: 400;
    line-height: 1.15;
  }
  .brand__name { font-size: 26px; letter-spacing: 2px; text-transform: uppercase; }
  .brand__place { font-size: 26px; letter-spacing: 2px; text-transform: uppercase; }

  .divider {
    position: absolute;
    left: 262px; top: 95px;
    width: 1px; height: 120px;
    background: var(--divider);
  }
  .contact {
    position: absolute;
    left: 290px; top: 92px;
    color: var(--navy);
  }
  .contact__name { font-weight: 800; font-size: 18px; margin-bottom: 8px; }
  .contact__list { list-style: none; font-weight: 300; font-size: 14.5px; line-height: 1.45; }
  .contact__list li { display: flex; align-items: flex-start; gap: 7px; }
  .contact__list svg { width: 12px; height: 12px; flex: none; margin-top: 4px; }

  .back-brand {
    position: absolute;
    left: 40px; top: 60px;
    width: 300px;
    text-align: center;
    color: var(--silver);
    font-weight: 400;
    font-size: 40px;
    letter-spacing: 4px;
    text-transform: uppercase;
    line-height: 1.1;
  }
  .bridge-art {
    position: absolute;
    right: 0; bottom: 0;
    width: 400px; height: 240px;
    background: linear-gradient(200deg, rgba(201,201,204,0.55) 0%, rgba(201,201,204,0.25) 55%, rgba(30,28,72,0) 100%);
    clip-path: polygon(100% 0, 100% 100%, 0 100%, 30% 55%, 70% 18%);
  }
</style>
</head>
<body>
  <section class="card card--front" aria-label="Business card front">
    <div class="brand">
      <div class="brand__name">Harborline</div>
      <div class="brand__place">Realty</div>
    </div>
    <div class="divider"></div>
    <div class="contact">
      <p class="contact__name">Name Lastname</p>
      <ul class="contact__list">
        <li>
          <svg viewBox="0 0 12 12" aria-hidden="true"><path d="M3 1 L5 3 L4 4.5 Q5 7 7.5 8 L9 7 L11 9 L9.5 11 Q2 10 1 2.5 Z" fill="var(--navy)"/></svg>
          <span>Office number: 813-555-0142</span>
        </li>
        <li>
          <svg viewBox="0 0 12 12" aria-hidden="true"><g fill="none" stroke="var(--navy)" stroke-width="1"><circle cx="6" cy="6" r="5"/><ellipse cx="6" cy="6" rx="2.2" ry="5"/><path d="M1 6 H11 M2 3.5 H10 M2 8.5 H10"/></g></svg>
          <span>www.harborlinerealty.com</span>
        </li>
        <li>
          <svg viewBox="0 0 12 12" aria-hidden="true"><path d="M6 0.5 A4 4 0 0 1 10 4.5 C10 7.5 6 11.5 6 11.5 C6 11.5 2 7.5 2 4.5 A4 4 0 0 1 6 0.5 Z" fill="var(--navy)"/><circle cx="6" cy="4.5" r="1.4" fill="var(--paper)"/></svg>
          <span>4120 West Harbor Blvd<br>Tampa, FL 33611</span>
        </li>
      </ul>
    </div>
  </section>

  <section class="card card--back" aria-label="Business card back">
    <div class="back-brand">Harborline<br>Realty</div>
    <div class="bridge-art" role="img" aria-label="Illustration of a cable-stayed bridge with two towers arching across the lower right corner"></div>
  </section>
</body>
</html>
```